TRV Business Card

Business card design for a handyman company. Want to portray a professional image and stay away from the "Mom & Pops" image that is normally associated with handyman companies.

Business

```html
<!DOCTYPE html>
<html lang="en">
<head>
<meta charset="utf-8">
<title>TRV Business Card</title>
<link rel="stylesheet" href="https://fonts.googleapis.com/css2?family=EB+Garamond:ital,wght@0,400;0,700;1,600&display=swap">
<style>
  :root {
    --navy: #1b1f4e;
    --card: #ffffff;
    --backdrop: #e9e9ec;
    --ink-soft: #3a3d5c;
  }
  html, body {
    margin: 0;
    padding: 0;
    width: 1200px;
    height: 800px;
    overflow: hidden;
    background: var(--backdrop);
  }
  .canvas {
    position: relative;
    width: 1200px;
    height: 800px;
    display: flex;
    align-items: center;
    justify-content: center;
  }
  .business-card {
    position: relative;
    width: 380px;
    height: 650px;
    background: var(--card);
    box-shadow: 0 6px 24px rgba(0, 0, 0, 0.12);
    overflow: hidden;
    font-family: "EB Garamond", Georgia, serif;
    color: var(--navy);
  }
  .brand-name {
    position: absolute;
    top: 48px;
    left: 0;
    right: 0;
    margin: 0;
    text-align: center;
    font-weight: 700;
    font-size: 58px;
    letter-spacing: 6px;
    line-height: 1;
  }
  .service-list {
    position: absolute;
    top: 190px;
    left: 0;
    right: 0;
    margin: 0;
    padding: 0;
    list-style: none;
    text-align: center;
    font-style: italic;
    font-weight: 600;
    font-size: 31px;
    line-height: 1.38;
  }
  .corner-bands {
    position: absolute;
    left: 0;
    top: 0;
    width: 380px;
    height: 650px;
  }
  .band { fill: var(--navy); }
  .contact-block {
    position: absolute;
    right: 22px;
    top: 378px;
    margin: 0;
    text-align: right;
    font-style: normal;
    font-size: 13px;
    line-height: 1.4;
    color: var(--ink-soft);
  }
</style>
</head>
<body>
  <main class="canvas">
    <article class="business-card">
      <h1 class="brand-name">TRV</h1>
      <ul class="service-list">
        <li>Home Repairs</li>
        <li>Handyman Services</li>
        <li>Drain Cleaning</li>
        <li>Carpet Cleaning</li>
      </ul>
      <address class="contact-block">
        18 Orchard Ave 210<br>
        Lakeview, KS 66000<br>
        p (555) 0142 [2201]<br>
        f (555) 0187 [2201]<br>
        info@trvcare.com
      </address>
      <svg class="corner-bands" viewBox="0 0 380 650" aria-hidden="true">
        <polygon class="band" points="18,650 380,478 380,490 42,650"/>
        <polygon class="band" points="78,650 380,508 380,650"/>
      </svg>
    </article>
  </main>
</body>
</html>
```